Create the BEST and COOLEST website for events and media company!

Hi there. I am a start-up events and conferences company with a twist, and we are seeking a highly modern website for our company Lumen Harbor Media. Our company believes that (like the social networking theory) that each and every one of us is connected to anyone on the planet in six connections or less. E.g. I know someone, who knows someone, who knows someone. Hence, the name Lumen Harbor Media.

I have included the copy for the website attached.

While we do have a business audience, they are in the fields of technology from the banking, health, government sector. We would like our website to be edgy, fresh and steer away from stuffy corporate images.

To give you an idea, our website menu tabs will be labelled:
HOME: This will include a corporate video that’s being created next week for me. However, please still design this page with a very striking background image that fills the whole page. You can run the copy and put a mock video for me to just see the layout (we can insert the finished video later).

ROCKSTARS: this will show pictures of highly powerful leaders speaking on stage; with a highly engaged audience watching. We want to show we have the world’s best technology International speakers “rockstars” who are the best in their game when it comes to talking about the future of technology.

LOCAL LEGENDS: like the international ‘rockstar’ speakers we would bring over to Australia to present; this LOCAL LEGENDS page should show we have the best home-grown Chief business people speaking at conferences and smaller powerful roundtable luncheons.

UNSUNG HEROES: this is more the people in the audience who ask questions on a microphone; those that attend the conferences; or a speaking to people at a conference.

THE BAND: this is like an ‘about us’ – just a funkier name to tie in with the theme of rockstars, etc.

THE PARTNERS: this is like a sponsor client page, where we invite people to partner with us and sponsor our events and conferences.

YOU & DORIAN FLECK: Dorian Fleck is a famous actor who made the term ‘six degrees of separation’ very popular. This page will have a little bit of an introduction, but mainly have the following video fill the landing page: https://www.vidstreamhub.example/watch?v=Qzt-plK4WB8

Website Functionality and Features:

• Try and make the ‘vibe’ and look and feel consistent, hip and modern (but still maintain a professional look). At the end of the day, people looking at our website are very senior business chiefs of organisations and also marketing chiefs.
• We may add more pages once we become established, so the website needs to ensure we can do that easily.
• We want pictures to not look stock photos. We want them to fresh, innovative, inspirational.
• Images should have a ‘wow’ factor. Like this one: https://www.stockframebank.example/detail/news-photo/general-view-of-crowd-during-brightloop-talks-2018-news-photo/481203967
• Need a mix of speaker, stage, audience, pictures. While we want to be fresh, edgy and contemporary we need to remember our viewers are the big chiefs of businesses – so lets try and have cool shots, but ensure there is a link to the business decision makers in a modern way. They all don’t have to wear suits, but not too casual either
• Other types of imagery I like is this one: https://www.stockframebank.example/detail/photo/smiling-audience-using-smart-phone-flashlights-for-royalty-free-image/372815094.
• The following are ok, not wow – but to give you an idea:
• https://www.stockframebank.example/detail/photo/smiling-male-speaker-in-wheelchair-on-stage-royalty-free-image/372816288
https://www.stockframebank.example/detail/photo/smiling-woman-with-camera-phone-in-dark-audience-royalty-free-image/372817452
https://www.stockframebank.example/detail/photo/audience-using-camera-phones-royalty-free-image/376630581
https://www.stockframebank.example/detail/photo/male-speaker-on-stage-talking-to-audience-royalty-free-image/372818736

NB: Logos are supplied in low resolution, but I can send you high resolution also
Updates

Hi there I will be adding two low-resolution images of my business partner and I for the ABOUT US page which is called THE BAND in the menu tab.

Hi everyone, thank you for your designs. I have uploaded a MAIN SCREEN IDEAS word document to give you further ideas of how the options I like for the main landing page on the home page. Hope this helps!

Target Market(s)

High end business people in marketing and business.

Coding

Coded - Design and coding required

Number of Pages Required

5+ page

Font styles to use
Sans Serif

Requirements
Must have
• Fresh, inspirational and aspirational designs. We need to make events and conferences look exciting and that we are bring the best technology speakers (like BrightLoop events) to our audience of marketing and technology professionals.
Should not have
• Cheesy, old stock photos; or pictures of American executives as this is for an Australian audience.
• PLEASE do not include an UPCOMING EVENTS or a SPEAKERS section as we will not be having this showcasing. You can feature ROCK STARS, LOCAL LEGENDS and UNSUNG HEROES if you like on the home page + the video of YOU and DORIAN FLECK (with his picture on the video box with a play button)

```html
<!DOCTYPE html>
<html lang="en">
<head>
<meta charset="utf-8">
<title>Lumen Harbor Media</title>
<link rel="stylesheet" href="https://fonts.googleapis.com/css2?family=Jost:wght@400;500&family=Open+Sans:wght@400;600&display=swap">
<style>
  :root {
    --ink: #1a1a1a;
    --night: #141414;
    --band-dark: #1c1c1c;
    --band-light: #2a2a2a;
    --paper: #ffffff;
    --mist: #f1f1f1;
    --body-text: #3a3a3a;
    --nav-text: #e6e6e6;
    --accent-red: #d62424;
    --frame-shadow: rgba(0, 0, 0, 0.22);
  }
  * { box-sizing: border-box; margin: 0; padding: 0; }
  html, body {
    width: 1200px;
    height: 3965px;
    overflow: hidden;
    background: var(--paper);
    color: var(--ink);
    font-family: "Open Sans", Arial, sans-serif;
  }
  .page { position: relative; width: 1200px; height: 3965px; }

  /* Header */
  .site-header {
    position: absolute; top: 0; left: 0; width: 1200px; height: 111px;
    background: var(--night);
    display: flex; align-items: center;
  }
  .brand {
    position: absolute; left: 142px; top: 34px;
    display: flex; align-items: center; gap: 10px;
    font-family: "Jost", Arial, sans-serif; font-weight: 500;
    font-size: 16px; letter-spacing: 1.5px; color: var(--paper);
  }
  .brand-dot { width: 14px; height: 14px; border-radius: 50%; background: var(--paper); }
  .main-nav {
    position: absolute; left: 378px; top: 66px;
    display: flex; gap: 26px;
    font-family: "Open Sans", Arial, sans-serif; font-size: 12px;
    color: var(--nav-text); letter-spacing: 0.3px;
  }

  /* Hero */
  .hero {
    position: absolute; top: 111px; left: 0; width: 1200px; height: 515px;
    background: linear-gradient(160deg, #4a3a30 0%, #7a5a44 35%, #3d3029 65%, #1f2430 100%);
  }
  .hero-play { position: absolute; left: 570px; top: 337px; }

  /* Intro */
  .intro {
    position: absolute; top: 690px; left: 145px; width: 910px;
    display: flex; gap: 50px;
    font-family: "Jost", Arial, sans-serif; font-size: 14px; line-height: 22px;
    color: var(--body-text);
  }
  .intro p { width: 430px; }

  /* Sections */
  .section { position: absolute; left: 0; width: 1200px; }
  .section-dark-band {
    position: absolute; left: 0; top: 0; width: 1200px;
    background: linear-gradient(90deg, var(--band-dark), var(--band-light) 50%, var(--band-dark));
  }
  .section-title {
    position: absolute; left: 0; width: 1200px; text-align: center;
    font-size: 27px; font-weight: 400; letter-spacing: 0.5px; color: var(--ink);
  }
  .section-copy {
    position: absolute; left: 170px; width: 860px; text-align: center;
    font-size: 13.5px; line-height: 23px; color: var(--body-text);
  }
  .on-dark .section-title { color: var(--paper); }
  .on-dark .section-copy { color: #dcdcdc; }
  .know-more { color: inherit; text-decoration: underline; font-weight: 600; }

  .photo-frame {
    position: absolute; border: 5px solid var(--paper);
    box-shadow: 0 2px 10px var(--frame-shadow);
  }

  .video-frame { position: absolute; background: #101010; box-shadow: 0 2px 10px var(--frame-shadow); }
  .video-screen {
    position: absolute; left: 8px; top: 8px; right: 8px; bottom: 30px;
    background: radial-gradient(ellipse at 50% 40%, #6a6a6a 0%, #3a3a3a 45%, #151515 80%);
  }
  .video-controls {
    position: absolute; left: 8px; right: 8px; bottom: 6px; height: 20px;
    display: flex; align-items: center; gap: 10px;
    font-size: 8px; color: #bbb; padding: 0 8px;
  }
  .progress-track { flex: 1; height: 3px; background: #444; position: relative; }
  .progress-fill { position: absolute; left: 0; top: 0; height: 3px; width: 80%; background: var(--accent-red); }

  .site-footer {
    position: absolute; left: 0; top: 3912px; width: 1200px; height: 53px;
    background: var(--night); color: #cfcfcf;
    font-size: 12px; display: flex; align-items: center; justify-content: center;
  }
</style>
</head>
<body>
<div class="page">

  <header class="site-header">
    <div class="brand"><span class="brand-dot"></span>LUMEN HARBOR MEDIA</div>
    <nav class="main-nav">
      <span>HOME</span><span>ROCKSTARS</span><span>LOCAL LEGENDS</span><span>UNSUNG HEROES</span><span>THE BAND</span><span>THE PARTNERS</span><span>YOU &amp; DORIAN FLECK</span>
    </nav>
  </header>

  <section class="hero" role="img" aria-label="Packed conference audience holding up orange cards as a speaker takes a selfie on stage">
    <svg class="hero-play" width="66" height="66" viewBox="0 0 66 66" aria-hidden="true">
      <circle cx="33" cy="33" r="30" fill="none" stroke="#ffffff" stroke-width="3"/>
      <path d="M26 20 L47 33 L26 46 Z" fill="none" stroke="#ffffff" stroke-width="3" stroke-linejoin="round"/>
    </svg>
  </section>

  <section class="intro">
    <p>We are a start-up events and conferences company with a twist, and we are seeking a highly modern website for our company Lumen Harbor Media. Our company believes that (like the social networking theory) that each and every one of us is connected to anyone on the planet in six connections or less. E.g. I know someone, who knows someone, who knows someone. Hence, the name Lumen Harbor Media.</p>
    <p>Lorem ipsum dolor sit amet, consectetuer adipiscing elit, sed diam nonummy nibh euismod tincidunt ut laoreet dolore magna aliquam erat volutpat. Ut wisi enim ad minim veniam, quis nostrud exerci tation ullamcorper suscipit lobortis nisl ut aliquip ex ea commodo consequat. Duis autem vel eum iriure dolor in hendrerit in vulputate velit esse molestie consequat, vel illum dolore eu feugiat nulla facilisis at vero eros et.</p>
  </section>

  <!-- You & Dorian Fleck -->
  <section class="section on-dark" style="top:899px;height:629px;">
    <div class="section-dark-band" style="height:290px;"></div>
    <h2 class="section-title" style="top:64px;">YOU &amp; DORIAN FLECK</h2>
    <p class="section-copy" style="top:106px;">Lorem ipsum dolor sit amet, consectetuer adipiscing elit, sed diam nonummy nibh euismod tincidunt ut laoreet dolore magna aliquam erat volutpat. Ut wisi enim ad minim veniam, quis nostrud exerci tation ullamcorper suscipit lobortis nisl ut aliquip…<a class="know-more">Know More</a></p>
    <div class="video-frame" style="left:272px;top:182px;width:656px;height:375px;">
      <div class="video-screen" role="img" aria-label="Black and white portrait of the actor on the video cover"></div>
      <svg width="60" height="44" viewBox="0 0 60 44" style="position:absolute;left:298px;top:150px;" aria-hidden="true">
        <rect width="60" height="44" rx="9" fill="#ffffff" fill-opacity="0.9"/>
        <path d="M24 13 L39 22 L24 31 Z" fill="#333333"/>
      </svg>
      <div class="video-controls">
        <span>0:00</span>
        <div class="progress-track"><div class="progress-fill"></div></div>
        <span>3:45</span>
      </div>
    </div>
  </section>

  <!-- Rockstars -->
  <section class="section" style="top:1528px;height:586px;background:var(--mist);">
    <h2 class="section-title" style="top:46px;">ROCKSTARS</h2>
    <p class="section-copy" style="top:88px;">Lorem ipsum dolor sit amet, consectetuer adipiscing elit, sed diam nonummy nibh euismod tincidunt ut laoreet dolore magna aliquam erat volutpat. Ut wisi enim ad minim veniam, quis nostrud exerci tation ullamcorper suscipit lobortis nisl ut aliquip…<a class="know-more">Know More</a></p>
    <div class="photo-frame" style="left:145px;top:158px;width:910px;height:368px;background:linear-gradient(135deg,#1d2a44 0%,#3a5a8a 40%,#7a8fb4 60%,#2a3450 100%);" role="img" aria-label="Smiling audience holding up phone flashlights at a concert-style event"></div>
  </section>

  <!-- Local Legends -->
  <section class="section" style="top:2114px;height:585px;background:var(--paper);">
    <h2 class="section-title" style="top:48px;">LOCAL LEGENDS</h2>
    <p class="section-copy" style="top:90px;">Lorem ipsum dolor sit amet, consectetuer adipiscing elit, sed diam nonummy nibh euismod tincidunt ut laoreet dolore magna aliquam erat volutpat. Ut wisi enim ad minim veniam, quis nostrud exerci tation ullamcorper suscipit lobortis nisl ut aliquip…<a class="know-more">Know More</a></p>
    <div class="photo-frame" style="left:145px;top:156px;width:910px;height:368px;background:linear-gradient(110deg,#3a2a22 0%,#6a5446 35%,#c9c2b8 60%,#4a3a30 100%);" role="img" aria-label="Executives seated at a long table during a roundtable luncheon"></div>
  </section>

  <!-- Unsung Heroes -->
  <section class="section" style="top:2699px;height:586px;background:var(--mist);">
    <h2 class="section-title" style="top:48px;">UNSUNG HEROES</h2>
    <p class="section-copy" style="top:90px;">Lorem ipsum dolor sit amet, consectetuer adipiscing elit, sed diam nonummy nibh euismod tincidunt ut laoreet dolore magna aliquam erat volutpat. Ut wisi enim ad minim veniam, quis nostrud exerci tation ullamcorper suscipit lobortis nisl ut aliquip…<a class="know-more">Know More</a></p>
    <div class="photo-frame" style="left:145px;top:161px;width:910px;height:367px;background:linear-gradient(120deg,#2a1a10 0%,#8a4a1e 35%,#d8a060 55%,#5a3a24 100%);" role="img" aria-label="Audience member asking a question into a microphone at a conference"></div>
  </section>

  <!-- About the Band -->
  <section class="section on-dark" style="top:3285px;height:627px;">
    <div class="section-dark-band" style="height:296px;"></div>
    <h2 class="section-title" style="top:68px;">ABOUT THE BAND</h2>
    <p class="section-copy" style="top:110px;">Lorem ipsum dolor sit amet, consectetuer adipiscing elit, sed diam nonummy nibh euismod tincidunt ut laoreet dolore magna aliquam erat volutpat. Ut wisi enim ad minim veniam, quis nostrud exerci tation ullamcorper suscipit lobortis nisl ut aliquip…<a class="know-more">Know More</a></p>
    <div class="photo-frame" style="left:272px;top:185px;width:656px;height:302px;background:linear-gradient(135deg,#142238 0%,#2f4e7a 40%,#8a9ab8 60%,#1a2638 100%);" role="img" aria-label="Smiling audience in a dark venue raising camera phones"></div>
  </section>

  <footer class="site-footer">Copyright © 2019 LUMEN HARBOR MEDIA. All Rights Reserved.</footer>

</div>
</body>
</html>
```